Clear Plastic Card Design

I am looking to have a business card designed from my logo icon. I am looking to match the style of a different business card I have attached in the files.
Looking for a card that is plastic, with layers of transparency in the shape of my logo icon (also attached in the files) - not a circle like the other card. The winning design will incorporate the red icon logo on the front and back and include the charity's name, "Lanterns for the Weary" in the same or similar font, as well as an email and phone number. For now, use the email: email@lanternsfortheweary.org and the phone number 555-318-4072.
We like how the sample business card has transparency, partial and full opacity layers and a matching color scheme. Files will need to be in vector so that our business card printing company can work with it.
UPDATE:
We've some excellent designs in, thank you everyone! I got an early review from the owner, and he requested a minor redirect to find his perfect design. He wants the design to stand out by NOT being a rectangle. Try instead a circle, square, or best yet - something that falls in the outline of the logo icon, either fully or partially. Thank you, everyone!
Contact Information for Business Card
Lanterns for the Weary text should be incorporated as well as a phone and email.
Look and feel

```html
<!DOCTYPE html>
<html lang="en">
<head>
<meta charset="utf-8">
<title>Lanterns for the Weary – Clear Card</title>
<link href="https://fonts.googleapis.com/css2?family=Sora:wght@400&family=Inter:wght@400;700&display=swap" rel="stylesheet">
<style>
  :root {
    --backdrop: #d8d1cd;
    --card-fill: rgba(255, 255, 255, 0.5);
    --card-edge: rgba(255, 255, 255, 0.95);
    --card-shade: rgba(150, 140, 135, 0.35);
    --brand-red: #c4161c;
    --ink: #1b1b1b;
  }
  * { margin: 0; padding: 0; box-sizing: border-box; }
  html, body { width: 1200px; height: 836px; overflow: hidden; background: var(--backdrop); }
  .stage { position: relative; width: 1200px; height: 836px; }
  .card-shape { position: absolute; inset: 0; }
  .brand-word {
    position: absolute; left: 300px; top: 360px;
    font-family: "Inter", sans-serif; font-weight: 700; font-size: 66px;
    color: var(--brand-red); letter-spacing: -1px;
  }
  .card-text { position: absolute; left: 679px; top: 272px; width: 250px; }
  .org-name {
    font-family: "Sora", sans-serif; font-weight: 400; font-size: 30px;
    line-height: 39px; color: var(--ink); letter-spacing: -0.5px;
    white-space: nowrap;
  }
  .person-name {
    margin-top: 14px;
    font-family: "Inter", sans-serif; font-weight: 700; font-size: 23px;
    color: var(--brand-red); letter-spacing: 0.3px;
  }
  .person-role {
    font-family: "Inter", sans-serif; font-weight: 400; font-size: 15px;
    color: var(--ink); margin-top: 1px;
  }
  .contact-list { list-style: none; margin-top: 14px; }
  .contact-list li {
    display: flex; align-items: center; gap: 7px;
    font-family: "Inter", sans-serif; font-size: 14px; color: var(--ink);
    height: 20.5px; white-space: nowrap;
  }
  .contact-list svg { width: 12px; height: 12px; fill: var(--brand-red); flex: none; }
</style>
</head>
<body>
<main class="stage">
  <svg class="card-shape" width="1200" height="836" viewBox="0 0 1200 836" aria-hidden="true">
    <path d="M323 244 H395 V236 Q395 208 423 208 H477 Q505 208 505 236 V244 H888
             Q968 244 968 330 V420 Q968 508 888 508 H505 V562 Q505 590 477 590 H423
             Q395 590 395 562 V462 H323 Q283 462 283 422 V284 Q283 244 323 244 Z"
          fill="var(--card-fill)" stroke="var(--card-edge)" stroke-width="2.5"/>
    <path d="M505 508 H888 Q968 508 968 420" fill="none" stroke="var(--card-shade)" stroke-width="1.5"/>
  </svg>

  <div class="brand-word">Lanterns</div>

  <section class="card-text">
    <h1 class="org-name">Lanterns for the<br>Weary</h1>
    <p class="person-name">MARCUS HALE</p>
    <p class="person-role">Founder &amp; CEO</p>
    <ul class="contact-list">
      <li>
        <svg viewBox="0 0 24 24"><path d="M6.6 10.8a15.1 15.1 0 0 0 6.6 6.6l2.2-2.2a1 1 0 0 1 1-.25 11.4 11.4 0 0 0 3.6.57 1 1 0 0 1 1 1V20a1 1 0 0 1-1 1A17 17 0 0 1 3 4a1 1 0 0 1 1-1h3.5a1 1 0 0 1 1 1c0 1.25.2 2.45.57 3.57a1 1 0 0 1-.25 1z"/></svg>
        555-318-4072
      </li>
      <li>
        <svg viewBox="0 0 24 24"><path d="M2 5h20v14H2z M2 5l10 8 10-8" stroke="#fff" stroke-width="1.5"/></svg>
        email@lanternsfortheweary.org
      </li>
      <li>
        <svg viewBox="0 0 24 24"><circle cx="12" cy="12" r="10"/><path d="M2 12h20M12 2c3 3 3 17 0 20M12 2c-3 3-3 17 0 20" stroke="#fff" stroke-width="1.5" fill="none"/></svg>
        lanternsfortheweary.org
      </li>
    </ul>
  </section>
</main>
</body>
</html>
```